Letterhead & Business Card for our Professional Practice (Financial Services)

We are looking for someone to design a letterhead and business card for our business, which is a professional practice called Corvel Brook Capital Limited. The website is at www.corvelbrookcapitel.example.

The letterhead needs to have: (a) our logo (b) address (c) telephone number (d) email address and (e) our company number.

We would like the stationary to be consistent with the website.

I have attached the logo in EPS and PNG format.

Target Market(s)

Professional services, large commercial enterprises, financial services

Industry/Entity Type

Financial Service

Font styles to use
Serif

Colors
3176b5
f04a50

Requirements
Must have
• Be consistent with our website located at www.corvelbrookcapital.example
• Be in the following formats:
• 1. Word template for the letterhead
• 2. PDF for the letterhead with setup and bleeds required at www.presslyne88.example
• 3. PDF for the business card with setup and bleeds required at www.presslyne88.example
Nice to have
• Something with a really interesting design that says "these guys are professional but dynamic and interesting"
Should not have
• Boring

```html
<!DOCTYPE html>
<html lang="en">
<head>
<meta charset="utf-8">
<title>Corvel Brook Capital — Stationery</title>
<link rel="stylesheet" href="https://fonts.googleapis.com/css2?family=Marcellus&family=PT+Serif:wght@400;700&display=swap">
<style>
:root{
  --navy:#0b3f72;
  --blue:#2f6ea8;
  --pale:#c9d8e8;
  --red:#d81f2f;
  --paper:#ffffff;
  --bg:#eef0f2;
  --ink:#333a42;
}
*{margin:0;padding:0;box-sizing:border-box}
html,body{width:1200px;height:937px;overflow:hidden;background:var(--bg)}
.canvas{position:relative;width:1200px;height:937px}
.sheet{position:absolute;background:var(--paper);overflow:hidden}
.sheet svg.wave{position:absolute;inset:0;width:100%;height:100%}
.brand{font-family:"Marcellus",serif;font-weight:400;color:var(--navy);white-space:nowrap}
.mark{position:absolute;background:var(--red)}
.small{font-family:"PT Serif",serif;color:var(--ink)}

/* letterhead */
.letterhead{left:185px;top:68px;width:388px;height:544px}
.letterhead .mark{left:59px;top:24px;width:38px;height:34px}
.letterhead .brand{position:absolute;left:16px;top:62px;font-size:17px}
.letter{position:absolute;left:36px;top:138px;width:300px;font-size:5.4px;line-height:7.6px}
.letter p{margin-bottom:7px}
.letter .gap{margin-bottom:22px}
.signature{width:40px;height:14px;background:linear-gradient(90deg,#9aa3ad,#d5d9de);margin:4px 0 8px}
.letter b{font-weight:700}
.contact{position:absolute;right:14px;top:452px;text-align:right;color:#fff;font-size:5.6px;line-height:7.4px}
.contact .row{margin-bottom:6px}

/* cover */
.cover{left:636px;top:40px;width:458px;height:576px}
.cover .mark{left:112px;top:413px;width:84px;height:80px}
.cover .brand{position:absolute;left:24px;top:502px;font-size:33px}
.cover .web{position:absolute;left:24px;top:553px;font-family:"PT Serif",serif;font-size:10px;letter-spacing:3px;color:var(--navy)}

/* business cards */
.card-front{left:45px;top:658px;width:178px;height:100px}
.card-front .brand{position:absolute;left:18px;top:81px;font-size:10.5px}
.card-front .person{position:absolute;right:8px;top:8px;text-align:right;font-size:6.4px;line-height:7px}
.card-front .person small{display:block;font-size:4px;letter-spacing:.5px}
.card-front .details{position:absolute;right:8px;top:30px;text-align:right;font-size:3.6px;line-height:6.4px}
.card-back{left:45px;top:785px;width:178px;height:99px}
.card-back .mark{left:76px;top:27px;width:24px;height:22px}
.card-back .brand{position:absolute;left:41px;top:53px;font-size:11px}

/* envelopes */
.env-front{left:265px;top:672px;width:431px;height:208px}
.env-front .mark{left:51px;top:22px;width:32px;height:30px}
.env-front .brand{position:absolute;left:15px;top:55px;font-size:13px}
.env-back{left:737px;top:672px;width:413px;height:208px}
.flap{position:absolute;left:0;top:0;width:100%;height:72px;background:var(--navy);border-radius:0 0 40px 40px}
.flap span{position:absolute;left:0;right:0;top:29px;text-align:center;color:#fff;font-family:"PT Serif",serif;font-size:10px;letter-spacing:3px}
</style>
</head>
<body>
<main class="canvas">

  <section class="sheet letterhead">
    <svg class="wave" viewBox="0 0 388 544" preserveAspectRatio="none" aria-hidden="true">
      <defs>
        <linearGradient id="lhFade" x1="0" y1="0" x2="1" y2="0">
          <stop offset="0" stop-color="#fff" stop-opacity="0"/>
          <stop offset="1" stop-color="#8fb0d0"/>
        </linearGradient>
      </defs>
      <path d="M0 520 C120 470 260 430 388 330 L388 360 C260 450 130 495 0 544 Z" fill="url(#lhFade)" opacity=".7"/>
      <path d="M60 544 C180 500 300 440 388 350 L388 544 Z" fill="var(--navy)"/>
      <path d="M60 544 C180 505 290 455 388 372 L388 385 C290 465 190 515 110 544 Z" fill="#3f74a8" opacity=".8"/>
    </svg>
    <div class="mark"></div>
    <div class="brand">Corvel Brook Capital</div>
    <div class="letter small">
      <p>July 2, 2012</p>
      <p><b>Dear Client,</b><br>Harlow House, Merton Lane, London</p>
      <p class="gap">We are pleased to confirm the arrangements discussed at our recent meeting. Our team has reviewed the figures you supplied and prepared a summary of options for the coming year. Each option sets out the expected costs, the timing of payments and the main risks involved. We would welcome the chance to walk through these with you in person and agree the next steps together.</p>
      <p class="gap">Please find the full schedule enclosed with this letter, together with the forms we need you to sign.</p>
      <p>Should you have any questions about the proposal, our advisers are available throughout the week. We can also arrange a call with your finance director to review the detail. Once we receive your instructions we will open the accounts and confirm each transfer in writing. Thank you for placing your trust in our practice.</p>
      <p>Best Regards,</p>
      <div class="signature" role="img" aria-label="Handwritten signature"></div>
      <p><b>Peter Halden</b><br>Director<br><br>Harlow House, Merton Lane, London</p>
    </div>
    <div class="contact small">
      <div class="row">14 Harlow Court,<br>Merton Lane</div>
      <div>020 5550 0142 ☏</div>
      <div>020 5550 0143 ▯</div>
      <div>020 5550 0144 ⎙</div>
      <div>office@corvelbrook.example ✉</div>
      <div>www.corvelbrookcapital.example ●</div>
      <div>Company No. 08412736</div>
    </div>
  </section>

  <section class="sheet cover">
    <svg class="wave" viewBox="0 0 458 576" preserveAspectRatio="none" aria-hidden="true">
      <defs>
        <linearGradient id="cvFade" x1="0" y1="0" x2="1" y2="0">
          <stop offset="0" stop-color="#fff" stop-opacity="0"/>
          <stop offset=".6" stop-color="#8fb0d0"/>
          <stop offset="1" stop-color="#3c6a9a"/>
        </linearGradient>
        <linearGradient id="cvSoft" x1="0" y1="0" x2="1" y2="0">
          <stop offset="0" stop-color="#fff" stop-opacity="0"/>
          <stop offset="1" stop-color="#c9d8e8"/>
        </linearGradient>
      </defs>
      <path d="M0 300 C100 220 230 210 330 300 C230 240 110 250 0 320 Z" fill="url(#cvSoft)" opacity=".8"/>
      <path d="M108 0 L150 0 C200 150 320 300 458 410 L458 470 C310 350 190 220 108 0 Z" fill="url(#cvFade)" opacity=".9"/>
      <path d="M70 0 L108 0 C150 160 290 330 458 460 L458 576 L448 576 C420 480 280 340 190 240 C120 160 85 70 70 0 Z" fill="var(--navy)"/>
      <path d="M108 0 L116 0 C160 160 300 320 458 440 L458 452 C290 330 150 170 108 0 Z" fill="#4f7fb0"/>
    </svg>
    <div class="mark"></div>
    <div class="brand">Corvel Brook Capital</div>
    <div class="web">www.corvelbrookcapital.example</div>
  </section>

  <section class="sheet card-front">
    <svg class="wave" viewBox="0 0 178 100" preserveAspectRatio="none" aria-hidden="true">
      <path d="M0 0 L80 0 C50 20 20 50 0 80 Z" fill="var(--navy)"/>
      <path d="M85 0 C55 25 25 55 8 100 L0 100 L0 85 C20 50 50 20 80 0 Z" fill="#8fb0d0" opacity=".8"/>
    </svg>
    <div class="brand">Corvel Brook Capital</div>
    <div class="person small"><b>ALAN MERCER</b><small>DIRECTOR</small></div>
    <div class="details small">14 Harlow Court<br>Merton Lane<br>020 5550 0142 ☏<br>020 5550 0143 ▯<br>020 5550 0144 ⎙<br>office@corvelbrook.example<br>www.corvelbrookcapital.example</div>
  </section>

  <section class="sheet card-back">
    <svg class="wave" viewBox="0 0 178 99" preserveAspectRatio="none" aria-hidden="true">
      <path d="M110 0 C150 30 160 60 178 99 L165 99 C150 60 135 30 100 0 Z" fill="var(--red)" opacity=".85"/>
      <path d="M120 0 C155 25 168 55 178 80 L178 60 C165 35 150 15 130 0 Z" fill="#f3a7ad"/>
    </svg>
    <div class="mark"></div>
    <div class="brand">Corvel Brook Capital</div>
  </section>

  <section class="sheet env-front">
    <svg class="wave" viewBox="0 0 431 208" preserveAspectRatio="none" aria-hidden="true">
      <path d="M290 0 C330 60 350 130 350 208 L340 208 C338 130 315 60 270 0 Z" fill="var(--red)"/>
      <path d="M300 0 C350 50 375 120 380 208 L360 208 C355 120 330 50 285 0 Z" fill="#f3a7ad" opacity=".7"/>
    </svg>
    <div class="mark"></div>
    <div class="brand">Corvel Brook Capital</div>
  </section>

  <section class="sheet env-back">
    <div class="flap"><span>www.corvelbrookcapital.example</span></div>
  </section>

</main>
</body>
</html>
```